Website redesign

Looking to redesign our existing website. (quill7meadows.com.au)
New design needs to be bright, fun and have an easy flowing.
The website needs to be design with call to action.

Some examples of other websites:
fernquaylo.com
tovanmilk.com.au

We are happy with the content of our existing website.

Target Market(s)

other businesses

Industry/Entity Type

Business Service

Number of Pages Required

5+ page

Requirements
Must have
• Theme redesign
Cool animation similar to fernquaylo.com

```html
<!DOCTYPE html>
<html lang="en">
<head>
<meta charset="utf-8">
<title>Virtual Assistant – FAQ | Quill7 Meadows</title>
<link href="https://fonts.googleapis.com/css2?family=Montserrat:wght@300;400;500;600;700;800&display=swap" rel="stylesheet">
<style>
:root{
  --blue:#14a6e2;
  --blue-soft:#cdeefb;
  --ink:#111b28;
  --body:#6b7178;
  --line:#e3e5e8;
  --navy:#0f1c2b;
  --navy-2:#16273a;
  --field:#f1f2f3;
  --white:#ffffff;
}
*{margin:0;padding:0;box-sizing:border-box}
html,body{width:1200px;height:3704px;overflow:hidden;background:var(--white)}
body{position:relative;font-family:'Montserrat',sans-serif;color:var(--ink)}
.abs{position:absolute}

/* header */
.brand{left:93px;top:26px;font-weight:700;font-size:30px;color:var(--ink);display:flex;align-items:center;gap:8px}
.brand .dot{width:14px;height:14px;border-radius:50%;background:var(--blue)}
.nav{right:93px;top:34px;display:flex;gap:24px;font-size:13.5px;font-weight:500}
.nav a{color:var(--ink);text-decoration:none}

/* hero */
.hero-title{left:167px;top:222px;z-index:2;font-weight:800;font-size:41px;line-height:43px;color:var(--blue);letter-spacing:1px;white-space:nowrap}
.hero-rule{left:167px;top:325px;width:138px;height:6px;background:var(--navy)}
.hero-art{left:612px;top:79px;width:451px;height:402px;z-index:1;border-radius:8px;background:linear-gradient(160deg,#eaf6fc 0%,#f4f5f6 60%,#ffffff 100%)}

/* intro */
.intro{left:0;width:1200px;text-align:center}
.intro h1{position:absolute;top:572px;width:100%;font-size:31px;font-weight:800;color:var(--blue);letter-spacing:1.5px}
.intro h2{position:absolute;top:624px;width:100%;font-size:21px;font-weight:700;letter-spacing:1px}
.chevrons{left:1086px;top:624px}

/* faq */
.cat{left:167px;font-size:19px;font-weight:700;letter-spacing:1.5px}
.q{left:545px;width:500px;display:flex;align-items:flex-start;gap:29px;font-size:12.8px;font-weight:700;letter-spacing:.5px;line-height:16px}
.q .ic{flex:0 0 20px;width:20px;height:20px;border-radius:50%;background:var(--blue);position:relative;margin-top:-2px}
.q .ic::before,.q .ic.plus::after{content:"";position:absolute;background:var(--white);left:5px;top:9px;width:10px;height:2px}
.q .ic.plus::after{left:9px;top:5px;width:2px;height:10px}
.q .ic.open{box-shadow:0 0 0 6px var(--blue-soft)}
.answer{left:594px;top:764px;width:445px;font-size:13.6px;font-weight:400;color:var(--body);line-height:22.5px;letter-spacing:.2px}
.answer p{margin-bottom:22.5px}
.rule{left:167px;width:868px;height:1px;background:var(--line)}

/* why section */
.why{left:0;top:2450px;width:1200px;height:582px;background:linear-gradient(135deg,var(--navy-2) 0%,var(--navy) 55%,#0b1622 100%)}
.why h3{position:absolute;top:78px;width:100%;text-align:center;color:var(--white);font-size:33px;font-weight:800}
.why h3 em{font-style:normal;color:var(--blue)}
.why .sub{position:absolute;top:136px;width:100%;text-align:center;color:var(--white);font-size:14px;font-weight:500}
.perk{position:absolute;width:240px;text-align:center;color:var(--white);font-size:15px;font-weight:700;line-height:20px}
.perk svg{display:block;margin:0 auto 14px}

/* quote */
.quote-photo{left:660px;top:2960px;width:346px;height:489px;z-index:0;border-radius:170px 170px 20px 20px;background:linear-gradient(180deg,#c99a74 0%,#eceff2 45%,#d9dde2 100%)}
.quote-title{left:208px;top:3116px;font-size:34px;font-weight:800}
.quote-title em{font-style:normal;color:var(--blue)}
.quote-sub{left:209px;top:3158px;font-size:14px;color:#555c63;line-height:18px}
.form{left:210px;top:3214px;width:450px;height:238px;background:var(--field);z-index:1}
.field{position:absolute;font-size:9.5px;color:#6b7178;border-bottom:1px solid #c9ccd0;padding-bottom:10px}
.submit{left:210px;top:3478px;width:145px;height:33px;background:var(--blue);color:var(--white);font-size:14px;font-weight:700;letter-spacing:1px;display:flex;align-items:center;justify-content:center;box-shadow:0 6px 14px rgba(20,166,226,.35)}
.consent{left:385px;top:3488px;display:flex;align-items:center;gap:8px;font-size:9.5px;color:#6b7178}
.consent i{width:13px;height:13px;border:1px solid #b9dcec;display:block;position:relative}
.consent i::after{content:"";position:absolute;left:3px;top:1px;width:4px;height:7px;border:solid var(--blue);border-width:0 1.5px 1.5px 0;transform:rotate(45deg)}

/* footer */
.footer{left:0;top:3582px;width:1200px;height:122px;background:var(--navy)}
.footer .brand{position:absolute;left:93px;top:44px;color:var(--white)}
.footer small{position:absolute;right:93px;top:56px;color:var(--white);font-size:10px;letter-spacing:.3px}
</style>
</head>
<body>

<header>
  <div class="abs brand">Quill7<span class="dot"></span></div>
  <nav class="abs nav"><a href="#">Home</a><a href="#">Our Story</a><a href="#">Tips and Tricks</a><a href="#">Contact Us</a><a href="#">FAQs</a></nav>
</header>

<section>
  <div class="abs hero-art" role="img" aria-label="Illustration of a person thinking beside a lightbulb thought bubble, with windows and a potted plant"></div>
  <div class="abs hero-title">VIRTUAL<br>ASSISTANT - FAQ</div>
  <div class="abs hero-rule"></div>
</section>

<section class="abs intro">
  <h1>HOW ARE YOU SPENDING YOUR TIME?</h1>
  <h2>TIME TO RECRUIT A VIRTUAL ASSISTANT...</h2>
</section>
<svg class="abs chevrons" width="66" height="40" viewBox="0 0 66 40" fill="none" stroke="#8a9096" stroke-width="2.2" stroke-linejoin="round">
  <path d="M20 4 4 20l16 16M36 4 20 20l16 16M52 4 36 20l16 16"/>
</svg>
<svg class="abs" style="left:85px;top:1066px" width="60" height="48" viewBox="0 0 60 48" fill="none" stroke="#9aa0a6" stroke-width="2">
  <rect x="2" y="10" width="56" height="35" rx="5"/><path d="M21 10V4h18v6M2 25h56M26 22h8v7h-8z"/>
</svg>
<svg class="abs" style="left:1118px;top:1680px" width="62" height="68" viewBox="0 0 62 68" fill="none" stroke="#9aa0a6" stroke-width="2">
  <path d="M31 3a28 28 0 1 1-14 52L9 64l3-13A28 28 0 0 1 31 3z"/><path d="M22 40 40 22"/><circle cx="23" cy="25" r="2.5"/><circle cx="39" cy="37" r="2.5"/>
</svg>

<main>
  <div class="abs cat" style="top:735px">RECRUITMENT</div>
  <div class="abs q" style="top:737px"><i class="ic open"></i><span>HOW DOES IT WORK?</span></div>
  <div class="abs answer">
    <p>Hiring a VA means you can scale your business quickly, easily and cost effectively. Sound like music to your ears? Fantastic! The full-time offshore staff report directly to you every business day and follow your business hours. They're basically an overseas extension of your local team!</p>
    <p>You get to define the standards of how they work as well as the systems and processes they follow. You also have direct access to them via phone, email and instant messaging. Think of them as the Angels to your Charlie!</p>
    <p>To get started, just give us a job description and we'll either hire from our existing talent or start the recruitment process based on your requirements. We handle the recruitment, background checks, testing and shortlisting. All you need to do is kick up your feet, pop open a cold one and choose who you'd like to interview.</p>
  </div>
  <div class="abs q" style="top:1183px"><i class="ic plus"></i><span>HOW LONG DOES THIS RECRUITMENT PROCESS TAKES?</span></div>
  <div class="abs rule" style="top:1240px"></div>

  <div class="abs cat" style="top:1275px">PRICING</div>
  <div class="abs q" style="top:1276px"><i class="ic plus"></i><span>DO YOUR FEES INCLUDE PHONE CHARGES?</span></div>
  <div class="abs q" style="top:1321px"><i class="ic plus"></i><span>HOW DO I PAY FOR OVERTIME?</span></div>
  <div class="abs q" style="top:1367px"><i class="ic plus" style="margin-top:6px"></i><span>HOW MUCH WILL IT COST AND WHAT'S INCLUDED IN<br>THE RATE?</span></div>
  <div class="abs q" style="top:1427px"><i class="ic plus"></i><span>DO I PAY FOR HOLIDAYS?</span></div>
  <div class="abs q" style="top:1473px"><i class="ic plus"></i><span>WILL I BE PAYING SALES TAX?</span></div>
  <div class="abs rule" style="top:1528px"></div>

  <div class="abs cat" style="top:1562px">BILLING</div>
  <div class="abs q" style="top:1563px"><i class="ic plus" style="margin-top:6px"></i><span>HOW DO YOU HANDLE ABSENCES? DO I GET REFUNDS<br>WHEN THE VA IS AWAY?</span></div>
  <div class="abs q" style="top:1625px"><i class="ic plus"></i><span>HOW AM I BILLED?</span></div>
  <div class="abs q" style="top:1670px"><i class="ic plus"></i><span>WHAT TYPE OF PAYMENT DO YOU ACCEPT?</span></div>
  <div class="abs rule" style="top:1727px"></div>

  <div class="abs cat" style="top:1761px">MANAGING THE VA'S</div>
  <div class="abs q" style="top:1762px"><i class="ic plus"></i><span>WILL YOU HELP ME TRAIN MY VA?</span></div>
  <div class="abs q" style="top:1808px"><i class="ic plus"></i><span>WHAT IF THE PERSON DOESN'T WORK OUT?</span></div>
  <div class="abs q" style="top:1853px"><i class="ic plus"></i><span style="white-space:nowrap">DO YOU DO PERFORMANCE AND SALARY EVALUATIONS?</span></div>
  <div class="abs q" style="top:1897px"><i class="ic plus"></i><span>CAN I GIVE THE VA AN INCREASE?</span></div>
  <div class="abs q" style="top:1942px"><i class="ic plus" style="margin-top:14px"></i><span>I'VE HEARD THAT INTERNET CONNECTION CAN BE BAD<br>IN THE PHILIPPINES. WHAT HAPPENS WHEN MY VA<br>CAN'T CONNECT TO THE INTERNET?</span></div>
  <div class="abs q" style="top:2021px"><i class="ic plus"></i><span>WHAT TYPE OF TASKS CAN I DELEGATE TO MY VA?</span></div>
  <div class="abs rule" style="top:2076px"></div>

  <div class="abs cat" style="top:2111px">CONTRACTS</div>
  <div class="abs q" style="top:2113px"><i class="ic plus"></i><span>DO I HAVE TO SIGN A CONTACT?</span></div>
  <div class="abs q" style="top:2157px"><i class="ic plus"></i><span>IS THE VA YOUR EMPLOYEE OR MINE?</span></div>
  <div class="abs q" style="top:2202px"><i class="ic plus"></i><span>HOW ABOUT THE SECURITY OF MY INFORMATION?</span></div>
  <div class="abs q" style="top:2248px"><i class="ic plus"></i><span style="white-space:nowrap">CAN I PURCHASE JUST A CERTAIN AMOUNT OF HOURS?</span></div>
  <div class="abs rule" style="top:2303px"></div>

  <div class="abs cat" style="top:2337px">BENEFITS</div>
  <div class="abs q" style="top:2338px"><i class="ic plus"></i><span>DOES MY VA GET PAID LEAVE<br>(SICK/VACATION/EMERGENCY) CREDITS?</span></div>
</main>

<section class="abs why">
  <h3>IT'S <em>QUILL7 MEADOWS</em></h3>
  <p class="sub">Why are we your new best outsourcing friend?</p>
  <div class="perk" style="left:157px;top:208px">
    <svg width="54" height="54" viewBox="0 0 54 54" fill="none" stroke="#14a6e2" stroke-width="2"><rect x="4" y="12" width="46" height="32" rx="3"/><circle cx="27" cy="26" r="5"/><path d="M18 42c1-6 17-6 18 0M20 50h14M36 6h10v8H36z"/></svg>
    Your Own Virtual<br>Assistant</div>
  <div class="perk" style="left:480px;top:208px">
    <svg width="54" height="54" viewBox="0 0 54 54" fill="none" stroke="#14a6e2" stroke-width="2"><rect x="8" y="3" width="38" height="48" rx="3"/><circle cx="34" cy="17" r="7"/><path d="M14 28h26M14 35h26M14 42h18"/></svg>
    One Invoice Per Month</div>
  <div class="perk" style="left:804px;top:208px">
    <svg width="54" height="54" viewBox="0 0 54 54" fill="none" stroke="#14a6e2" stroke-width="2"><path d="M20 6h14l-4 8h-6zM18 16h18c8 6 12 14 12 22 0 8-6 12-21 12S6 46 6 38c0-8 4-16 12-22z"/><circle cx="27" cy="34" r="8"/><path d="M23 38l8-8"/></svg>
    No Super or TAX</div>
  <div class="perk" style="left:157px;top:378px">
    <svg width="56" height="48" viewBox="0 0 56 48" fill="none" stroke="#14a6e2" stroke-width="2"><rect x="3" y="9" width="50" height="35" rx="3"/><path d="M20 9V3h16v6M3 24h50M24 21h8v7h-8z"/></svg>
    Dedicated To Your<br>Business Only</div>
  <div class="perk" style="left:480px;top:378px">
    <svg width="54" height="54" viewBox="0 0 54 54" fill="none" stroke="#14a6e2" stroke-width="2"><rect x="15" y="2" width="24" height="50" rx="3"/><path d="M23 7h8M25 46h4M28 22l-3 6h5l-3 6"/></svg>
    Dedicated Phone System</div>
  <div class="perk" style="left:804px;top:378px">
    <svg width="58" height="58" viewBox="0 0 58 58" fill="none" stroke="#14a6e2" stroke-width="2"><rect x="3" y="4" width="44" height="34" rx="2"/><circle cx="25" cy="18" r="6"/><path d="M16 30h18M30 36h24v14H38l-6 5v-5"/></svg>
    IT Setup and Support</div>
</section>

<section>
  <div class="abs quote-photo" role="img" aria-label="Photo of a smiling support agent wearing a headset and holding a tablet"></div>
  <svg class="abs" style="left:100px;top:3063px" width="56" height="50" viewBox="0 0 56 50" fill="none" stroke="#9aa0a6" stroke-width="2"><path d="M8 3h40a5 5 0 0 1 5 5v22a5 5 0 0 1-5 5H30l10 12-18-12H8a5 5 0 0 1-5-5V8a5 5 0 0 1 5-5z"/><circle cx="19" cy="19" r="1.5"/><circle cx="28" cy="19" r="1.5"/><circle cx="37" cy="19" r="1.5"/></svg>
  <div class="abs quote-title">GET A <em>QUOTE</em></div>
  <div class="abs quote-sub">Fill in the form below to get a Quote<br>for your own personal Virtual Assistant</div>
  <form class="abs form">
    <div class="field" style="left:34px;top:31px;width:403px">Business Name</div>
    <div class="field" style="left:34px;top:76px;width:187px">First Name</div>
    <div class="field" style="left:251px;top:76px;width:186px">Last Name</div>
    <div class="field" style="left:34px;top:120px;width:187px">Contact Number</div>
    <div class="field" style="left:251px;top:120px;width:186px">Email ID</div>
    <div class="field" style="left:34px;top:163px;width:403px;padding-bottom:34px">Describe the tasks you'll need from your Virtual Assistant</div>
  </form>
  <div class="abs submit">SUBMIT</div>
  <div class="abs consent"><i></i>Subscribe to our newsletter</div>
</section>

<footer class="abs footer">
  <div class="brand">Quill7<span class="dot"></span></div>
  <small>© 2020 QUILL7 MEADOWS | ALL RIGHTS RESERVED.</small>
</footer>

</body>
</html>
```